A5 Flyer for Financial Services Business

I am after a re-design of our business flyer to fit in with our new branding style and logo colour scheme. Wanting something with a bit of designer flair that I could not create myself. I have included the flyer which I created which lacks style so dazzle me.

I want to use the same content.

Text for main body of flyer is

Are you a small business owner, tradie or PAVC Service Provider struggling to stay on top of your bookkeeping and compliance obligations? If so we would love to help you get back on track and take control of your business finances so that you can make informed business decisions and focus on what you do best.

We have over 20 years industry experience and, as a small business ourselves, we are able to offer our clients a personal bookkeeping solution tailored to meet the needs of your business.

Accounts Payable | Accounts Receivable
Customer Invoicing
Bank and Credit Card Reconciliations
Payroll | Superannuation | Payroll Tax
Business Activity | Instalment Activity Statements
Regular Financial Reports
Tallyo and Bookwise Set-Up and Training

```html
<!DOCTYPE html>
<html lang="en">
<head>
<meta charset="utf-8">
<title>Even Ledger Financial Services – Bookkeeping Flyer</title>
<link rel="stylesheet" href="https://fonts.googleapis.com/css2?family=Bebas+Neue&family=Jost:wght@400;500&family=Oswald:wght@400;500;600&display=swap">
<style>
:root{
  --teal:#14a39a;
  --teal-dark:#0b6b6a;
  --teal-light:#7fd3cb;
  --ink:#1c1c1c;
  --charcoal:#3a3a3c;
  --silver-1:#f2f2f2;
  --silver-2:#b9b9b9;
  --badge:#d9d9d9;
  --paper:#f7f7f7;
  --white:#ffffff;
}
*{box-sizing:border-box;margin:0;padding:0}
html,body{width:892px;height:1200px;overflow:hidden;background:var(--paper)}
.flyer{position:relative;width:892px;height:1200px;overflow:hidden;
  background:linear-gradient(160deg,#ffffff 0%,#eeeeee 45%,#fafafa 60%,#e6e6e6 100%);
  font-family:"Jost",sans-serif;color:var(--ink)}
.shapes{position:absolute;inset:0}
.brand{position:absolute;left:55px;top:112px;display:flex;align-items:center;gap:10px}
.brand-mark{width:22px;height:22px;background:var(--teal-dark)}
.brand-name{font-family:"Jost",sans-serif;font-weight:400;font-size:25px;line-height:1.05;color:var(--teal-dark);letter-spacing:.5px}
.headline{position:absolute;left:62px;top:222px;font-family:"Bebas Neue",sans-serif;font-weight:400;font-size:74px;line-height:64px;color:var(--white);text-shadow:2px 3px 4px rgba(0,0,0,.35)}
.intro{position:absolute;left:59px;top:532px;width:385px;font-size:18.5px;line-height:24px;text-align:justify;text-align-last:left}
.intro p+p{margin-top:24px}
.credentials{position:absolute;left:59px;top:893px;width:265px}
.credential{display:block;height:26px;margin-bottom:6px;padding-left:7px;font-family:"Oswald",sans-serif;font-weight:500;font-size:19px;line-height:26px;color:var(--white);
  background:linear-gradient(90deg,var(--teal-dark),var(--teal) 60%)}
.seal-note{position:absolute;left:188px;top:1010px;font-family:"Oswald",sans-serif;font-weight:400;font-size:14px;line-height:14px;color:var(--charcoal)}
.service{position:absolute;width:168px;height:128px;border-radius:8px;
  background:linear-gradient(120deg,var(--silver-2) 0%,var(--silver-1) 40%,#cfcfcf 70%,#f4f4f4 100%);
  border-right:3px solid var(--teal);border-bottom:3px solid var(--teal);
  box-shadow:0 2px 4px rgba(0,0,0,.2);
  display:flex;align-items:center;justify-content:center;text-align:center;padding:26px 4px 4px;
  font-family:"Oswald",sans-serif;font-weight:600;font-size:18.5px;line-height:17.5px;text-transform:uppercase;color:var(--ink)}
.service-icon{position:absolute;left:50%;top:-47px;width:70px;height:70px;margin-left:-35px;border-radius:50%;
  background:radial-gradient(circle at 40% 35%,var(--teal) 0%,var(--teal-dark) 100%);border:3px solid #f5f5f5;
  display:flex;align-items:center;justify-content:center}
.service-icon svg{width:38px;height:38px;fill:none;stroke:var(--white);stroke-width:2;stroke-linecap:round;stroke-linejoin:round}
.phone{position:absolute;left:42px;top:1128px;display:flex;align-items:center;gap:10px;font-family:"Oswald",sans-serif;font-weight:600;font-size:42px;line-height:50px;color:var(--white)}
.web{position:absolute;left:372px;top:1156px;display:flex;align-items:center;gap:12px;font-family:"Oswald",sans-serif;font-weight:500;font-size:26px;line-height:40px;color:var(--white)}
</style>
</head>
<body>
<main class="flyer">
  <svg class="shapes" width="892" height="1200" viewBox="0 0 892 1200">
    <defs>
      <linearGradient id="bandFill" x1="0" y1="0" x2="1" y2="0.4">
        <stop offset="0" stop-color="#0b6b6a"/>
        <stop offset=".55" stop-color="#14a39a"/>
        <stop offset="1" stop-color="#9adcd5"/>
      </linearGradient>
      <linearGradient id="photoFill" x1="0" y1="0" x2="1" y2="1">
        <stop offset="0" stop-color="#6fc7bf"/>
        <stop offset=".35" stop-color="#5d7fa0"/>
        <stop offset=".7" stop-color="#d9dde2"/>
        <stop offset="1" stop-color="#3b3f46"/>
      </linearGradient>
      <linearGradient id="footerFill" x1="0" y1="0" x2="1" y2="0">
        <stop offset="0" stop-color="#0b6b6a"/>
        <stop offset=".7" stop-color="#14a39a"/>
        <stop offset="1" stop-color="#7fd3cb"/>
      </linearGradient>
    </defs>
    <path class="photo" role="img" aria-label="Photo of a businessman reviewing charts on a tablet at a desk with a calculator and notebook"
      d="M525 31 H892 V377 H440 V179 Q478 179 490 150 L505 60 Q512 31 525 31Z" fill="url(#photoFill)"/>
    <path class="hero-band" d="M0 179 H600 V377 H575 Q555 377 540 400 L480 475 Q462 500 430 500 H0Z" fill="url(#bandFill)" opacity=".95"/>
    <path class="swoosh" d="M530 28 Q505 30 492 70 L470 140 Q455 185 395 190 Q430 175 448 140 L478 62 Q495 26 530 28Z" fill="#8a8a8a"/>
    <path class="swoosh" d="M600 378 Q565 378 548 404 L488 478 Q470 505 425 505 Q462 496 478 472 L535 398 Q555 372 600 378Z" fill="#7d7d7d"/>
    <circle class="badge-placeholder" role="img" aria-label="Registered practitioner badge" cx="114" cy="1034" r="56" fill="var(--badge)"/>
    <g class="growth-icon" fill="none" stroke="#14a39a" stroke-width="7" stroke-linecap="round">
      <circle cx="345" cy="1045" r="24"/>
      <line x1="328" y1="1063" x2="308" y2="1088"/>
      <text x="345" y="1055" fill="#14a39a" stroke="none" font-family="Oswald,sans-serif" font-weight="600" font-size="28" text-anchor="middle">$</text>
      <g fill="#14a39a" stroke="none">
        <rect x="372" y="1078" width="9" height="22"/><rect x="386" y="1068" width="9" height="32"/>
        <rect x="400" y="1055" width="9" height="45"/><rect x="414" y="1040" width="9" height="60"/>
        <rect x="428" y="1028" width="9" height="72"/>
        <rect x="350" y="1100" width="92" height="6"/>
      </g>
    </g>
    <path class="footer-band" d="M0 1115 H345 L370 1200 H0Z" fill="url(#footerFill)"/>
    <path class="footer-dark" d="M355 1151 H892 V1200 H370Z" fill="#3a3a3c"/>
  </svg>

  <div class="brand"><span class="brand-mark"></span><span class="brand-name">Even Ledger<br>Financial Services</span></div>

  <h1 class="headline">Bookkeeping<br>tailored to<br>your business<br>needs</h1>

  <section class="intro">
    <p>Are you a small business owner, tradie or PAVC Service Provider struggling to stay on top of your bookkeeping and compliance obligations? If so we would love to help you get back on track and take control of your business finances so that you can make informed business decisions and focus on what you do best.</p>
    <p>We have over 20 years industry experience and, as a small business ourselves, we are able to offer our clients a personal bookkeeping solution tailored to meet the needs of your business.</p>
  </section>

  <div class="credentials">
    <span class="credential">TALLYO CERTIFIED ADVISOR</span>
    <span class="credential">BOOKWISE PRO ADVISOR</span>
  </div>
  <p class="seal-note">BAS agent<br>12345678</p>

  <div class="service" style="left:584px;top:452px">
    <span class="service-icon"><svg viewBox="0 0 40 40"><rect x="6" y="14" width="14" height="20" rx="2"/><path d="M9 19h8M9 24h2M13 24h2M9 29h2M13 29h2"/><path d="M18 6h14v26H22"/><path d="M22 12h6M22 17h6"/></svg></span>
    Accounts<br>Payable /<br>Accounts<br>Receivable
  </div>
  <div class="service" style="left:500px;top:627px">
    <span class="service-icon"><svg viewBox="0 0 40 40"><path d="M8 4h18l6 6v24H8z"/><path d="M12 14h16M12 19h16M12 24h10"/><path d="M24 30l3 3 6-7"/></svg></span>
    Customer<br>Invoicing
  </div>
  <div class="service" style="left:681px;top:627px">
    <span class="service-icon"><svg viewBox="0 0 40 40"><rect x="4" y="12" width="28" height="18" rx="2"/><path d="M8 8h28v18"/><rect x="8" y="17" width="6" height="4"/><path d="M8 25h18"/></svg></span>
    Bank and<br>Credit Card<br>Reconciliations
  </div>
  <div class="service" style="left:500px;top:806px">
    <span class="service-icon"><svg viewBox="0 0 40 40"><path d="M4 18l16 11 16-11v18H4z"/><path d="M4 18l6-5M36 18l-6-5"/><rect x="11" y="5" width="18" height="16"/><circle cx="20" cy="13" r="4"/></svg></span>
    Payroll /<br>Superannuation<br>/ Payroll Tax
  </div>
  <div class="service" style="left:681px;top:806px">
    <span class="service-icon"><svg viewBox="0 0 40 40"><rect x="9" y="4" width="18" height="30" rx="3"/><circle cx="18" cy="16" r="5"/><path d="M24 24v-4l3 1v5l6 2-2 8h-8l-4-6"/></svg></span>
    Business<br>Activity<br>Instalment /<br>Activity<br>Statements
  </div>
  <div class="service" style="left:500px;top:986px">
    <span class="service-icon"><svg viewBox="0 0 40 40"><path d="M8 4h18l6 6v26H8z"/><path d="M12 30v-4M17 30v-7M22 30v-5M12 12h8M12 17h8"/><circle cx="27" cy="20" r="4"/></svg></span>
    Regular<br>Financial<br>Reports
  </div>
  <div class="service" style="left:681px;top:986px">
    <span class="service-icon"><svg viewBox="0 0 40 40"><rect x="16" y="5" width="20" height="15"/><path d="M20 10h12M20 14h8"/><circle cx="9" cy="10" r="3"/><path d="M5 34V18h8l5-3M9 34v-8M26 20v6l-5 8M26 26l5 8"/></svg></span>
    Tallyo and<br>Bookwise<br>Set-up and<br>Training
  </div>

  <div class="phone">
    <svg width="30" height="30" viewBox="0 0 30 30"><circle cx="15" cy="15" r="13" fill="none" stroke="#fff" stroke-width="3"/><path d="M10 8l3 4-2 2q2 4 5 5l2-2 4 3-2 3q-6 0-10-6t0-9z" fill="#fff"/></svg>
    0400 123 456
  </div>
  <div class="web">
    <svg width="20" height="20" viewBox="0 0 20 20" fill="none" stroke="#fff" stroke-width="1.5"><circle cx="10" cy="10" r="8.5"/><ellipse cx="10" cy="10" rx="4" ry="8.5"/><path d="M1.5 10h17M3 5.5h14M3 14.5h14"/></svg>
    www.evenledgerfinancial.com.au
  </div>
</main>
</body>
</html>
```